Long Term Insurance for Maturing Women

My business, is a Full service Life and Property Insurance Agency.. I want a reply card, Gloss, with woman showing Maturity, on a beach looking out at a Sun Set, with light Colors of Rainbow.
Thinking: If I am alone, how much income will I need to pay for a Long Term Sickness or Injury. ?
Do I have enough money set aside to cover the added expenses of a long Term Illness ?
Have I enough Life Insurance to cover final expenses, and leave my love ones free of any Debt from my Passing ?
These are real life's concerns, Please Call, let's start finding answers today !
Mark Doverby, Agent # 0718243 at (555-203-4817) - Halvert Insurance & Financial Service LLC.
Markdov@halvertins.example 4100 Birchwell Rd, Cypress Ca. 90000

Industry/Entity Type

Business

```html
<!DOCTYPE html>
<html lang="en">
<head>
<meta charset="utf-8">
<title>Long Term Insurance for Maturing Women – Reply Card</title>
<link rel="stylesheet" href="https://fonts.googleapis.com/css2?family=Tinos:wght@400;700&family=Arimo:wght@400&display=swap">
<style>
  :root {
    --stage: #2b2b2b;
    --ink: #1b1b1b;
    --band: #0d0d0d;
    --paper: #ffffff;
    --title-veil: rgba(245, 232, 215, 0.72);
    --sunset-top: #8a6a48;
    --sunset-mid: #d99a55;
    --sunset-glow: #f3c27e;
    --sand-dark: #3a2717;
    --haze-light: #f4efe9;
    --haze-mid: #e2d9cf;
    --beach-light: #f6efe6;
    --beach-mid: #d9c9b6;
    --beach-dark: #a8927b;
    --rule: #111111;
  }
  * { margin: 0; padding: 0; box-sizing: border-box; }
  html, body { width: 900px; height: 1200px; overflow: hidden; }
  body { background: var(--stage); position: relative; font-family: "Tinos", "Times New Roman", serif; color: var(--ink); }

  .card { position: absolute; left: 25px; width: 850px; overflow: hidden; background: var(--paper); }
  .card--front { top: 35px; height: 548px; }
  .card--back { top: 611px; height: 549px; }

  /* Front */
  .sunset-photo {
    position: absolute; left: 0; top: 0; width: 372px; height: 548px;
    background:
      radial-gradient(ellipse 220px 160px at 190px 430px, var(--sunset-glow) 0%, rgba(243,194,126,0) 100%),
      linear-gradient(180deg, var(--sunset-top) 0%, var(--sunset-mid) 62%, var(--sunset-glow) 78%, var(--sand-dark) 82%, var(--sand-dark) 100%);
  }
  .title-box {
    position: absolute; left: 0; top: 28px; width: 345px; height: 97px;
    background: var(--title-veil); padding: 16px 0 0 17px;
  }
  .title {
    font-weight: 700; font-size: 26px; line-height: 33px; color: var(--ink);
    text-shadow: 1px 1px 2px rgba(0,0,0,0.25);
  }
  .portrait-photo {
    position: absolute; left: 372px; top: 0; width: 478px; height: 548px;
    background:
      radial-gradient(ellipse 200px 260px at 300px 160px, var(--haze-mid) 0%, rgba(226,217,207,0) 100%),
      linear-gradient(180deg, var(--haze-light), #f8f5f1);
  }
  .concerns { position: absolute; left: 397px; top: 55px; width: 450px; list-style: none; }
  .concerns li {
    position: relative; padding-left: 16px; font-size: 15px; line-height: 25px; margin-bottom: 7px;
  }
  .concerns li::before {
    content: "›"; position: absolute; left: 0; top: -2px; font-family: "Arimo", sans-serif; font-weight: 700; font-size: 20px;
  }
  .tagline { position: absolute; left: 413px; top: 233px; font-family: "Arimo", Arial, sans-serif; font-size: 23px; color: var(--ink); }
  .call { position: absolute; left: 413px; top: 283px; display: flex; gap: 8px; }
  .call svg { flex: none; margin-top: 2px; }
  .call p { font-weight: 700; font-size: 24px; line-height: 31px; }
  .agent { position: absolute; right: 20px; top: 360px; text-align: right; font-size: 18.5px; line-height: 25px; }
  .contact-band {
    position: absolute; left: 0; top: 482px; width: 850px; height: 40px; background: var(--band);
    color: var(--paper); font-size: 24px; line-height: 40px; text-align: center;
  }

  /* Back */
  .beach-photo {
    position: absolute; inset: 0;
    background:
      radial-gradient(ellipse 260px 200px at 520px 110px, #fffaf2 0%, rgba(255,250,242,0) 100%),
      linear-gradient(160deg, var(--beach-mid) 0%, var(--beach-light) 35%, var(--beach-light) 55%, var(--beach-mid) 75%, var(--beach-dark) 100%);
  }
  .divider { position: absolute; left: 456px; top: 46px; width: 2px; height: 458px; background: var(--rule); }
  .stamp-box { position: absolute; left: 695px; top: 56px; width: 79px; height: 103px; border: 1.5px dashed #3a2a20; }
  .address-line { position: absolute; left: 499px; width: 274px; height: 2px; background: var(--rule); }
</style>
</head>
<body>
  <section class="card card--front">
    <div class="sunset-photo" role="img" aria-label="Silhouette of a mature woman sitting on a beach facing a golden sunset over the sea"></div>
    <div class="title-box"><h1 class="title">Long Term Insurance for<br>Maturing Women</h1></div>
    <div class="portrait-photo" role="img" aria-label="Soft, faded photo of a woman in a knit cap resting by the window"></div>
    <ul class="concerns">
      <li>If I am alone, how much income will I need to pay for a Long Term Sickness or Injury ?</li>
      <li>Do I have enough money set aside to cover the added expenses of a long Term Illness ?</li>
      <li>Have I enough Life Insurance to cover final expenses, and leave my love ones free of any Debt from my Passing ?</li>
    </ul>
    <p class="tagline">These are real life's concerns</p>
    <div class="call">
      <svg width="28" height="28" viewBox="0 0 28 28" aria-hidden="true">
        <circle cx="14" cy="14" r="13" fill="#1b1b1b"/>
        <path d="M9.5 7.5c.8-.5 1.6-.3 2 .4l1.3 2.3c.4.7.2 1.4-.4 1.8l-.9.6c.7 1.6 1.9 2.9 3.4 3.8l.6-.9c.4-.6 1.2-.8 1.8-.4l2.3 1.3c.7.4.9 1.2.4 2l-.8 1.2c-.6.8-1.6 1.1-2.6.8-4.4-1.5-7.6-4.8-9-9.2-.3-1 0-2 .8-2.6z" fill="#ffffff"/>
      </svg>
      <p>Please Call, let's start finding<br>&nbsp;answers today !</p>
    </div>
    <p class="agent">Mark Doverby, Agent # 0718243<br>at (555-203-4817) - Halvert<br>Insurance &amp; Financial<br>Service LLC</p>
    <p class="contact-band">Markdov@halvertins.example 4100 Birchwell Rd, Cypress Ca. 90000</p>
  </section>

  <section class="card card--back">
    <div class="beach-photo" role="img" aria-label="Faded photo of a woman sitting on the sand by the sea with palm trees and soft sunlight"></div>
    <div class="divider"></div>
    <div class="stamp-box"></div>
    <div class="address-line" style="top:231px"></div>
    <div class="address-line" style="top:292px"></div>
    <div class="address-line" style="top:351px"></div>
    <div class="address-line" style="top:411px"></div>
  </section>
</body>
</html>
```